Healthy lifestyle Influencer business card

I need your creativity to have a business card that I can leave in all the restaurants, hotels and spas I visit to inform them that I am an influencer specializing in the wellness sector and that I will write a review about them. You can use my instagram photos Velusport72 or on my website www.piattileggerinuovi.it. I would like my business card to impress with its creativity! thank you very much!

Contact Information for Business Card

siteweb, instagram, phone number

Font styles to use
Decorative
Script

Colors
0094D4
00A9DD
6FCCEA
C7EBF8
E9F6FB
59FF00
82FF00
B8FF75
E3FFCB
F4FFEA
FFC000
F8CF3A
FAE287
FDF2CF
FEFAEE
F0912C
F2A743
F7CA91
FBE8D2
FDF5EE
EE7325
F08F49
F5BC92
FAE3D3
FDF4ED
EB3D1F
EC4F4E
F09395
F8D3D4
FCEDEE
E54698
E96AAD
F1A4CE
F9D9EA
FCEFF6

Requirements
Nice to have
• creativity

```html
<!DOCTYPE html>
<html lang="it">
<head>
<meta charset="utf-8">
<title>Velia Light Kitchen – Business Card</title>
<link rel="stylesheet" href="https://fonts.googleapis.com/css2?family=Quicksand:wght@400;500;600&family=Poiret+One&display=swap">
<style>
  :root {
    --backdrop: #c8c8c8;
    --card-white: #ffffff;
    --aqua: #a5dcdd;
    --aqua-light: #c4e9ea;
    --veil: rgba(255, 255, 255, 0.86);
    --ink: #4a4a4a;
    --ink-soft: #555555;
    --icon: #333333;
  }
  * { margin: 0; padding: 0; box-sizing: border-box; }
  html, body {
    width: 1200px;
    height: 1200px;
    overflow: hidden;
    background: var(--backdrop);
  }
  .canvas {
    position: relative;
    width: 1200px;
    height: 1200px;
  }
  .card {
    position: absolute;
    left: 192px;
    width: 817px;
    height: 454px;
    overflow: hidden;
  }
  .card--front { top: 124px; background: var(--aqua); }
  .card--back { top: 622px; background: var(--card-white); }

  .front-pattern {
    position: absolute;
    inset: 0;
    background:
      radial-gradient(circle at 12% 30%, var(--aqua-light) 0, transparent 28%),
      radial-gradient(circle at 88% 70%, var(--aqua-light) 0, transparent 28%),
      radial-gradient(circle at 30% 85%, var(--aqua-light) 0, transparent 22%),
      radial-gradient(circle at 75% 18%, var(--aqua-light) 0, transparent 22%),
      var(--aqua);
  }
  .front-veil {
    position: absolute;
    left: 240px;
    top: 58px;
    width: 338px;
    height: 338px;
    border-radius: 50%;
    background: var(--veil);
  }
  .brand {
    position: absolute;
    text-align: center;
    color: var(--ink);
  }
  .brand__name {
    font-family: "Quicksand", sans-serif;
    font-weight: 500;
    font-size: 35px;
    line-height: 1;
    color: var(--ink);
    white-space: nowrap;
  }
  .brand__tagline {
    font-family: "Quicksand", sans-serif;
    font-weight: 600;
    font-size: 17px;
    line-height: 1;
    color: var(--ink-soft);
    margin-top: 16px;
    white-space: nowrap;
  }
  .brand__tagline sup { font-size: 9px; vertical-align: 7px; }
  .card--front .brand { left: 0; width: 817px; top: 200px; }
  .card--back .brand { left: 30px; width: 320px; top: 207px; }
  .card--back .brand__name { font-size: 31px; }
  .card--back .brand__tagline { font-size: 15px; margin-top: 14px; }

  .divider {
    position: absolute;
    left: 350px;
    top: 148px;
    width: 2px;
    height: 170px;
    background: var(--ink);
  }
  .contact-list {
    position: absolute;
    left: 378px;
    top: 133px;
    list-style: none;
  }
  .contact {
    display: flex;
    align-items: center;
    height: 68px;
  }
  .contact__icon {
    width: 27px;
    height: 27px;
    flex: none;
    margin-right: 21px;
  }
  .contact__text {
    font-family: "Poiret One", sans-serif;
    font-size: 29px;
    color: var(--ink);
    white-space: nowrap;
  }
  .contact__text--web { letter-spacing: 0.6px; }
</style>
</head>
<body>
<main class="canvas">

  <section class="card card--front" aria-label="Fronte del biglietto">
    <div class="front-pattern" role="img" aria-label="Motivo decorativo di rametti bianchi con bacche su fondo acqua"></div>
    <div class="front-veil"></div>
    <div class="brand">
      <p class="brand__name">Velia Light Kitchen</p>
      <p class="brand__tagline">Leggera con i piatti che ami<sup>®</sup></p>
    </div>
  </section>

  <section class="card card--back" aria-label="Retro del biglietto">
    <div class="brand">
      <p class="brand__name">Velia Light Kitchen</p>
      <p class="brand__tagline">Leggera con i piatti che ami<sup>®</sup></p>
    </div>
    <div class="divider"></div>
    <ul class="contact-list">
      <li class="contact">
        <svg class="contact__icon" viewBox="0 0 28 28" aria-hidden="true">
          <circle cx="14" cy="14" r="14" fill="var(--icon)"/>
          <path d="M9.2 7.5c.5-.4 1.2-.3 1.5.2l1.6 2.4c.3.5.2 1.1-.2 1.4l-1 .8c.7 1.6 2 3 3.6 3.8l.8-1c.4-.4 1-.5 1.4-.2l2.4 1.6c.5.3.6 1 .2 1.5l-1 1.2c-.6.7-1.6.9-2.4.5-3.5-1.6-6.2-4.3-7.7-7.8-.4-.8-.2-1.8.5-2.4z" fill="#fff"/>
        </svg>
        <span class="contact__text">008 412 735 9021</span>
      </li>
      <li class="contact">
        <svg class="contact__icon" viewBox="0 0 28 28" aria-hidden="true">
          <circle cx="14" cy="14" r="14" fill="var(--icon)"/>
          <g fill="none" stroke="#fff" stroke-width="1">
            <circle cx="14" cy="14" r="7"/>
            <ellipse cx="14" cy="14" rx="3" ry="7"/>
            <line x1="7" y1="14" x2="21" y2="14"/>
            <line x1="8" y1="10.5" x2="20" y2="10.5"/>
            <line x1="8" y1="17.5" x2="20" y2="17.5"/>
          </g>
        </svg>
        <span class="contact__text contact__text--web">www.piattileggerinuovi.it</span>
      </li>
      <li class="contact">
        <svg class="contact__icon" viewBox="0 0 28 28" aria-hidden="true">
          <circle cx="14" cy="14" r="14" fill="var(--icon)"/>
        </svg>
        <span class="contact__text">@Velusport72</span>
      </li>
    </ul>
  </section>

</main>
</body>
</html>
```